I'm a bed retailer and require 4x Banners for my new website to stand out.

I require 4x banners / pictures. Size required for every banner.
360px wide, 360px high
I have attached each picture which needs resizing and adding writing within the image stating the following
1x Metal
1x Wooden
1x Fabric
1x Leather
Font styles to use
Sans Serif
Colors
0555a3
85acd3
ffc214
Requirements
Must have
- Names attached to each image

```html
<!DOCTYPE html>
<html lang="en">
<head>
<meta charset="utf-8">
<title>Bed Frames – Buying made simple</title>
<link rel="stylesheet" href="https://fonts.googleapis.com/css2?family=League+Spartan:wght@500;700&family=Didact+Gothic&family=Arimo:wght@700&display=swap">
<style>
  :root{
    --brand-blue:#0555a3;
    --brand-light-blue:#85acd3;
    --brand-yellow:#ffc214;
    --tile-blue:#0064b1;
    --tile-yellow:#ffc20e;
    --tile-grey:#474747;
    --tile-red:#d52027;
    --navy:#0a3c6e;
    --text-dark:#333;
    --text-grey:#555;
    --offer-red:#d7262e;
    --white:#fff;
  }
  *{margin:0;padding:0;box-sizing:border-box}
  html,body{width:1200px;height:805px;overflow:hidden;background:var(--white)}
  body{position:relative;font-family:"Didact Gothic",sans-serif;color:var(--text-dark)}

  .promo-strip{position:absolute;left:0;top:0;width:1200px;height:24px;background:#d10a0a;overflow:hidden}
  .promo-strip span{position:absolute;left:0;right:0;top:-12px;text-align:center;color:var(--white);font:700 20px "Arimo",sans-serif;letter-spacing:1px}

  .section-title{position:absolute;left:0;width:1200px;text-align:center;font-size:16px;color:var(--text-dark)}
  .intro-title{top:43px}
  .frames-title{top:315px}
  .frames-sub{position:absolute;top:342px;left:540px;width:122px;text-align:center;font-size:10px;color:var(--white);background:#2b6fe0;line-height:13px}

  .benefit{position:absolute;top:86px;width:204px;height:204px;color:var(--white);font-family:"League Spartan",sans-serif;font-weight:700;text-transform:uppercase}
  .benefit--credit{left:175px;background:var(--tile-blue)}
  .benefit--delivery{left:390px;background:var(--tile-yellow)}
  .benefit--returns{left:606px;background:var(--tile-grey)}
  .benefit--savings{left:822px;background:var(--tile-red)}
  .benefit .line{position:absolute;left:18px;right:18px;white-space:nowrap;line-height:1}

  .credit-rate{top:40px;font-size:70px;letter-spacing:-2px}
  .credit-note{position:absolute;left:128px;top:42px;font-size:21px;line-height:20px}
  .credit-note small{display:block;font-size:12px;line-height:12px}
  .credit-fast{top:112px;font-size:22px;border-top:1px solid rgba(255,255,255,.5);padding-top:6px}
  .credit-apply{top:136px;font-size:36px}

  .delivery-free{top:36px;font-size:76px;letter-spacing:1px}
  .delivery-word{top:110px;font-size:38px;color:rgba(255,255,255,.92)}
  .delivery-min{top:150px;font-size:14px;border-top:1px solid rgba(255,255,255,.5);padding-top:6px}

  .returns-days{top:50px;font-size:32px;font-weight:500;letter-spacing:1px}
  .returns-quibble{top:88px;font-size:44px;border-top:1px solid rgba(255,255,255,.4);padding-top:4px}
  .returns-word{top:136px;font-size:44px;border-top:1px solid rgba(255,255,255,.4);padding-top:4px}

  .savings-head{top:34px;font-size:38px;letter-spacing:1px}
  .savings-upto{position:absolute;left:18px;top:78px;font-size:24px;line-height:24px;border-top:1px solid rgba(255,255,255,.5);padding-top:6px;width:168px}
  .savings-pct{position:absolute;left:60px;top:86px;font-size:58px;line-height:1}
  .savings-less{top:136px;font-size:38px;border-top:1px solid rgba(255,255,255,.5);padding-top:6px}

  .frame-card{position:absolute;top:371px;width:208px;height:208px}
  .frame-card--fabric{left:175px}
  .frame-card--metal{left:390px}
  .frame-card--wooden{left:608px}
  .frame-card--leather{left:822px}
  .frame-photo{height:163px}
  .frame-card--fabric .frame-photo{background:linear-gradient(160deg,#c9c7c9,#6c6a74 55%,#e8e6e3)}
  .frame-card--metal .frame-photo{background:linear-gradient(170deg,#7c7f84,#cfd1d3 50%,#eceae6)}
  .frame-card--wooden .frame-photo{background:linear-gradient(160deg,#e9e6e0,#9aa4b3 55%,#d8c7ab)}
  .frame-card--leather .frame-photo{background:linear-gradient(160deg,#8c6a58,#a45f33 55%,#5b5d66)}
  .frame-label{height:45px;display:flex;align-items:center;justify-content:center;font:700 40px "Arimo",sans-serif;letter-spacing:-.5px}
  .frame-card--fabric .frame-label{background:var(--brand-yellow);color:var(--brand-blue)}
  .frame-card--metal .frame-label{background:var(--brand-blue);color:var(--brand-yellow)}
  .frame-card--wooden .frame-label{background:var(--navy);color:var(--brand-yellow)}
  .frame-card--leather .frame-label{background:var(--brand-yellow);color:var(--brand-blue)}

  .offer-banner{position:absolute;left:2px;top:600px;width:1198px;height:200px;background:linear-gradient(175deg,#f2f2f2,#dcdcdc 40%,#f6f6f6 70%,#e2e2e2)}
  .offer-banner::after{content:"";position:absolute;left:8px;top:7px;right:8px;bottom:7px;border:1px solid rgba(255,255,255,.9)}
  .offer-headline{position:absolute;left:0;width:1198px;top:32px;text-align:center;font:700 42px "League Spartan",sans-serif;color:var(--offer-red);letter-spacing:2px}
  .offer-text{position:absolute;left:0;width:1198px;top:84px;text-align:center;font-size:28px;color:var(--text-grey);letter-spacing:1px}
  .offer-button{position:absolute;left:547px;top:128px;width:106px;height:33px;background:var(--tile-blue);color:var(--white);font:700 11px "Arimo",sans-serif;display:flex;align-items:center;justify-content:center;z-index:1}
  .mascot{position:absolute;left:942px;top:14px;width:134px;height:166px;border-radius:40px;background:radial-gradient(circle at 50% 45%,#2a79c4,#1d5ea4 60%,rgba(255,255,255,0) 72%);z-index:1}
</style>
</head>
<body>
  <div class="promo-strip"><span>Savings "up to" 60% less everyday</span></div>

  <h2 class="section-title intro-title">Buying made simple</h2>

  <div class="benefit benefit--credit">
    <div class="line credit-rate">0%</div>
    <div class="credit-note"><small>Interest</small>Free<small>Credit</small></div>
    <div class="line credit-fast">Fast and easy</div>
    <div class="line credit-apply">To apply</div>
  </div>
  <div class="benefit benefit--delivery">
    <div class="line delivery-free">Free</div>
    <div class="line delivery-word">Delivery</div>
    <div class="line delivery-min">On orders over £50</div>
  </div>
  <div class="benefit benefit--returns">
    <div class="line returns-days">14 day no</div>
    <div class="line returns-quibble">Quibble</div>
    <div class="line returns-word">Returns</div>
  </div>
  <div class="benefit benefit--savings">
    <div class="line savings-head">Savings</div>
    <div class="savings-upto">Up<br>to</div>
    <div class="savings-pct">60%</div>
    <div class="line savings-less">Less</div>
  </div>

  <h2 class="section-title frames-title">Looking for a Bed Frame</h2>
  <div class="frames-sub">What takes your fancy?</div>

  <a class="frame-card frame-card--fabric">
    <div class="frame-photo" role="img" aria-label="Grey tufted fabric bed in a bedroom"></div>
    <div class="frame-label">Fabric</div>
  </a>
  <a class="frame-card frame-card--metal">
    <div class="frame-photo" role="img" aria-label="Chrome metal bed frame with lamp"></div>
    <div class="frame-label">Metal</div>
  </a>
  <a class="frame-card frame-card--wooden">
    <div class="frame-photo" role="img" aria-label="White and oak wooden bed with grey throw"></div>
    <div class="frame-label">Wooden</div>
  </a>
  <a class="frame-card frame-card--leather">
    <div class="frame-photo" role="img" aria-label="Tan leather bed against a brick wall"></div>
    <div class="frame-label">Leather</div>
  </a>

  <section class="offer-banner" role="img" aria-label="Close-up of a quilted white mattress">
    <div class="offer-headline">WOW! 10% OFF</div>
    <div class="offer-text">Any Mattress, when you buy any Bedframe</div>
    <div class="offer-button">Shop Now</div>
    <div class="mascot" role="img" aria-label="Cartoon mattress mascot waving"></div>
  </section>
</body>
</html>
```